Corwin Crest Homes Needs Business Card Design

Looking for a unique modern business card to fit my new Logo.
Name: Marcus Corwin
Company: Corwin Crest Homes, LLC
Tag Line: Crafted With Care
Email: corwincresthomes@mailnest.example
Phone: (555) 017-2846
Website: www.corwincresthomes.example
License: CORWICH462KX

```html
<!DOCTYPE html>
<html lang="en">
<head>
<meta charset="utf-8">
<title>Corwin Crest Homes — Business Card</title>
<link rel="stylesheet" href="https://fonts.googleapis.com/css2?family=Arimo:wght@400;700&display=swap">
<style>
  :root {
    --backdrop: #e4e4e4;
    --card-white: #f6f6f6;
    --house-blue: #3a96c8;
    --house-blue-deep: #2f8bc0;
    --outline-black: #050505;
    --ink: #111111;
    --card-dark: #2c2c2c;
    --text-light: #ffffff;
    --mark-grey: #8a8a8a;
  }
  html, body {
    margin: 0;
    width: 1200px;
    height: 1200px;
    overflow: hidden;
    background: var(--backdrop);
    font-family: "Arimo", Arial, sans-serif;
  }
  .sheet {
    position: relative;
    width: 1200px;
    height: 1200px;
  }
  .card {
    position: absolute;
    left: 150px;
    width: 800px;
    height: 457px;
    border-radius: 22px;
    overflow: hidden;
    transform: scale(1.125);
    transform-origin: top left;
  }
  .card-front { top: 56px; background: var(--card-white); }
  .card-back {
    top: 630px;
    background: linear-gradient(180deg, #333333 0%, var(--card-dark) 100%);
  }
  .house-panel { position: absolute; inset: 0; }
  .brand {
    position: absolute;
    left: 30px;
    top: 150px;
    width: 280px;
    display: flex;
    align-items: center;
    justify-content: center;
    gap: 10px;
    color: var(--ink);
    font-weight: 700;
    font-size: 24px;
    white-space: nowrap;
  }
  .brand-square {
    width: 16px;
    height: 16px;
    background: var(--house-blue);
  }
  .contact {
    position: absolute;
    left: 402px;
    right: 0;
    top: 170px;
    text-align: center;
    color: var(--text-light);
  }
  .contact p { margin: 0; }
  .contact-name { font-weight: 700; font-size: 30px; line-height: 34px; }
  .contact-role { font-size: 17px; line-height: 20px; }
  .rule {
    width: 44px;
    height: 1px;
    background: var(--text-light);
    margin: 10px auto 14px;
  }
  .contact-company { font-size: 19px; line-height: 22px; margin-bottom: 12px !important; }
  .contact-line { font-size: 19px; line-height: 24px; }
  .contact-licence { font-size: 19px; line-height: 22px; }
  .back-name {
    position: absolute;
    left: 0; right: 0;
    top: 170px;
    text-align: center;
    color: var(--mark-grey);
    font-weight: 700;
    font-size: 46px;
  }
  .tagline {
    position: absolute;
    left: 0; right: 0;
    top: 380px;
    margin: 0;
    text-align: center;
    color: var(--text-light);
    font-size: 22px;
  }
</style>
</head>
<body>
<main class="sheet">
  <section class="card card-front" aria-label="Card front">
    <svg class="house-panel" viewBox="0 0 800 457" aria-hidden="true">
      <polygon points="373,160 600,34 800,150 800,457 373,457" fill="var(--outline-black)"/>
      <defs>
        <linearGradient id="blueFill" x1="0" y1="0" x2="0" y2="1">
          <stop offset="0" stop-color="var(--house-blue)"/>
          <stop offset="1" stop-color="var(--house-blue-deep)"/>
        </linearGradient>
      </defs>
      <polygon points="402,177 600,66 800,180 800,457 402,457" fill="url(#blueFill)"/>
    </svg>
    <div class="brand"><span class="brand-square"></span>Corwin Crest Homes</div>
    <div class="contact">
      <p class="contact-name">MARCUS CORWIN</p>
      <p class="contact-role">Residential Builder</p>
      <div class="rule"></div>
      <p class="contact-company">Corwin Crest Homes, LLC</p>
      <p class="contact-line">(555) 017-2846</p>
      <p class="contact-line">corwincresthomes@mailnest.example</p>
      <p class="contact-line">www.corwincresthomes.example</p>
      <div class="rule"></div>
      <p class="contact-licence">Lic : CORWICH462KX</p>
    </div>
  </section>

  <section class="card card-back" aria-label="Card back">
    <div class="back-name">Corwin Crest Homes</div>
    <p class="tagline">Crafted With Care</p>
  </section>
</main>
</body>
</html>
```